Dental Specialist Needs a Business Card

We are a state of the art dental specialty office and need a business card that looks modern but professional.
I have provided our logo design in both vertical and horizontal. We use the design on letterhead in the vertical format but provided both forms for you. Thanks

Please add the address, phone and fax numbers I listed to all designs and please leave a space for website and for my employee name on each design. Thanks 2847 Halloway Avenue, Suite K East Marlow, NY 14391 Phone (716)382-9157 Fax:(716)382-9150 My name is Miles R.Dunford,D.D.S. If you want to show it with my name but the design needs to allow for the name to be switched.

Industry/Entity Type

Business

```html
<!DOCTYPE html>
<html lang="en">
<head>
<meta charset="utf-8">
<title>Keystone Endodontics – Business Card</title>
<link href="https://fonts.googleapis.com/css2?family=Open+Sans:wght@400;600&display=swap" rel="stylesheet">
<style>
  :root{
    --page:#e9eaec;
    --card:#ffffff;
    --blue:#3d9ad9;
    --green:#7cc242;
    --ink:#2b2b2b;
    --muted:#555a60;
    --shadow:rgba(0,0,0,.18);
  }
  *{margin:0;padding:0;box-sizing:border-box}
  html,body{width:1200px;height:900px;overflow:hidden}
  body{background:var(--page);font-family:"Open Sans",Arial,sans-serif;position:relative}

  .business-card{
    position:absolute;left:180px;top:210px;width:840px;height:480px;
    background:var(--card);box-shadow:0 10px 30px var(--shadow);overflow:hidden;
  }
  .brand{
    position:absolute;left:30px;top:150px;width:370px;
    display:flex;flex-direction:column;align-items:center;gap:18px;text-align:center;
  }
  .brand-dot{width:64px;height:64px;border-radius:50%;background:var(--blue)}
  .brand-name{font-weight:600;font-size:24px;color:var(--ink);letter-spacing:.3px;white-space:nowrap}

  .info-panel{
    position:absolute;left:430px;top:0;right:0;bottom:34px;background:var(--card);
    box-shadow:-14px 0 22px -12px var(--shadow);
  }
  .contact{position:absolute;left:50px;top:120px}
  .person-name{font-size:24px;color:var(--blue);font-weight:400;line-height:1.2}
  .person-role{font-size:16px;color:var(--muted);margin-bottom:18px}
  .contact-list{list-style:none}
  .contact-list li{display:flex;align-items:flex-start;gap:12px;font-size:15px;color:var(--muted);line-height:1.5;margin-bottom:4px}
  .contact-list svg{width:14px;height:14px;margin-top:4px;flex:none;fill:var(--blue)}
  .fax-label{font-size:11px;font-weight:600;color:var(--blue);width:14px;margin-top:2px;flex:none}

  .corner-mark{position:absolute;right:30px;bottom:52px;width:40px;height:40px;border-radius:50%;background:var(--blue)}

  .band{position:absolute;bottom:0;height:34px}
  .band-blue{left:0;width:430px;height:26px;background:var(--blue)}
  .band-green{left:430px;right:0;background:var(--green)}
</style>
</head>
<body>
  <article class="business-card">
    <div class="brand">
      <span class="brand-dot"></span>
      <span class="brand-name">Keystone Endodontics P.C.</span>
    </div>

    <section class="info-panel">
      <div class="contact">
        <p class="person-name">Dana Whitlock</p>
        <p class="person-role">Designation</p>
        <ul class="contact-list">
          <li>
            <svg viewBox="0 0 16 16"><path d="M3 1h3l1.5 4-2 1.2a9 9 0 0 0 4.3 4.3L11 8.5l4 1.5v3a2 2 0 0 1-2 2A13 13 0 0 1 1 3a2 2 0 0 1 2-2z"/></svg>
            <span>(716)382-9157</span>
          </li>
          <li>
            <span class="fax-label">Fx</span>
            <span>(716)382-9150</span>
          </li>
          <li>
            <svg viewBox="0 0 16 16"><circle cx="8" cy="8" r="7" fill="none" stroke="#3d9ad9" stroke-width="1.6"/><path d="M1 8h14M8 1c3 3 3 11 0 14M8 1c-3 3-3 11 0 14" fill="none" stroke="#3d9ad9" stroke-width="1.2"/></svg>
            <span>www.webaddress.com</span>
          </li>
          <li>
            <svg viewBox="0 0 16 16"><path d="M8 0a5.5 5.5 0 0 0-5.5 5.5C2.5 10 8 16 8 16s5.5-6 5.5-10.5A5.5 5.5 0 0 0 8 0zm0 8a2.5 2.5 0 1 1 0-5 2.5 2.5 0 0 1 0 5z"/></svg>
            <span>2847 Halloway Avenue, Suite K<br>East Marlow, NY 14391</span>
          </li>
        </ul>
      </div>
    </section>

    <span class="corner-mark"></span>

    <div class="band band-blue"></div>
    <div class="band band-green"></div>
  </article>
</body>
</html>
```